Brennick Drilling Inc. Business card design

Business card design for "Brennick Drilling Inc. - Directional Drilling Services"

Address is:

Brennick Drilling Inc.
512 - 73 Tarvel Crescent SW
Calgary, Alberta, Canada
T2K 4P8

Please incorporate the logo design into the card, thank you.

Target Market(s)

Oil & Gas and Drilling

Industry/Entity Type

Business

```html
<!DOCTYPE html>
<html lang="en">
<head>
<meta charset="utf-8">
<title>Brennick Drilling Inc. – Business Cards</title>
<link href="https://fonts.googleapis.com/css2?family=Michroma&family=Arimo:wght@400&display=swap" rel="stylesheet">
<style>
  :root {
    --backdrop: #f3f3f3;
    --paper: #ffffff;
    --ink: #0a0a0a;
    --brand-red: #d21f0c;
    --text-light: #ffffff;
    --mark-grey: #8a8a8a;
    --pattern-light: #ececec;
    --pattern-mid: #e2e2e2;
  }
  * { box-sizing: border-box; margin: 0; padding: 0; }
  html, body {
    width: 1200px; height: 900px; overflow: hidden;
    background: var(--backdrop);
  }
  .canvas { position: relative; width: 1200px; height: 900px; }

  .card {
    position: absolute; top: 305px;
    width: 473px; height: 289px; overflow: hidden;
  }
  .card--front { left: 98px; background: var(--paper); }
  .card--back { left: 629px; background: var(--ink); }

  /* front */
  .front__pattern {
    position: absolute; left: 100px; top: 0; width: 373px; height: 174px;
    background: radial-gradient(ellipse at 70% 30%, var(--pattern-mid) 0%, var(--pattern-light) 45%, var(--paper) 80%);
  }
  .brand {
    position: absolute; left: 0; width: 100%;
    display: flex; flex-direction: column; align-items: center;
  }
  .front__brand { top: 40px; }
  .brand__dot {
    width: 62px; height: 62px; border-radius: 50%;
    border: 3px solid var(--brand-red);
    margin-bottom: 22px;
  }
  .brand__name {
    font-family: "Michroma", sans-serif;
    font-size: 13px; letter-spacing: 0.3px;
    text-transform: uppercase; white-space: nowrap;
  }
  .front__brand .brand__name { color: var(--ink); }

  .front__band {
    position: absolute; left: 0; top: 174px; width: 100%; height: 13px;
    background: var(--brand-red);
    display: flex; align-items: center; justify-content: center;
  }
  .tagline {
    font-family: "Arimo", sans-serif; font-size: 6.5px;
    letter-spacing: 3px; text-transform: uppercase;
  }
  .front__band .tagline { color: var(--text-light); }

  .front__contact {
    position: absolute; left: 0; top: 187px; width: 100%; height: 102px;
    background: var(--ink);
  }
  .address {
    position: absolute; left: 117px; top: 27px; width: 200px;
    text-align: center; font-style: normal;
    font-family: "Arimo", sans-serif; font-size: 13px; line-height: 16.5px;
    color: var(--text-light);
  }

  /* back */
  .back__brand { top: 93px; }
  .back__brand .brand__dot {
    width: 70px; height: 70px; border-color: var(--mark-grey);
    margin-bottom: 14px;
  }
  .back__brand .brand__name { color: var(--mark-grey); font-size: 12px; }
  .back__brand .tagline { color: var(--mark-grey); margin-top: 2px; font-size: 6.5px; }
</style>
</head>
<body>
<main class="canvas">
  <section class="card card--front" aria-label="Business card front">
    <div class="front__pattern" role="img" aria-label="Faint grey decorative drill-bit pattern"></div>
    <div class="brand front__brand">
      <span class="brand__dot"></span>
      <h1 class="brand__name">Brennick Drilling Inc.</h1>
    </div>
    <div class="front__band"><p class="tagline">Directional Drilling Services</p></div>
    <div class="front__contact">
      <address class="address">
        512 - 73 Tarvel Crescent SW<br>
        Calgary, Alberta, Canada<br>
        T2K 4P8
      </address>
    </div>
  </section>

  <section class="card card--back" aria-label="Business card back">
    <div class="brand back__brand">
      <span class="brand__dot"></span>
      <h2 class="brand__name">Brennick Drilling Inc.</h2>
      <p class="tagline">Directional Drilling Services</p>
    </div>
  </section>
</main>
</body>
</html>
```